- Morvandi Customer Service Signs
- 60 year old financial services firm in Boston's financial district, stock brokers are our clients, we've young/energetic employees and it's critical they provide unbeatable customer service to the brokers, family atmosphere

```html
<!DOCTYPE html>
<html lang="en">
<head>
<meta charset="utf-8">
<title>Morvandi Customer Service Signs</title>
<link rel="stylesheet" href="https://fonts.googleapis.com/css2?family=Jost:wght@400;500;700;800&display=swap">
<style>
  :root {
    --page: #ffffff;
    --blue-deep: #12208a;
    --blue-mid: #1f3fc4;
    --blue-glow: #2d5be0;
    --orange: #f15a22;
    --gold: #b8924e;
    --white: #ffffff;
    --ink: #0b0b14;
    --stone: #9a9ca4;
    --skin: #c9926b;
  }
  html, body {
    margin: 0;
    padding: 0;
    width: 1200px;
    height: 314px;
    overflow: hidden;
    background: var(--page);
  }
  .sign-series {
    position: relative;
    width: 1200px;
    height: 314px;
    font-family: "Jost", "Century Gothic", sans-serif;
  }
  .sign {
    position: absolute;
    top: 17px;
    width: 216px;
    height: 283px;
    overflow: hidden;
    background: radial-gradient(ellipse at 55% 55%, var(--blue-glow) 0%, var(--blue-mid) 40%, var(--blue-deep) 100%);
  }
  .sign--rocks { left: 17px; }
  .sign--advocates { left: 261px; }
  .sign--perception { left: 499px; }
  .sign--mediocrity { left: 736px; }
  .sign--smart { left: 968px; }

  .stripes {
    position: absolute;
    inset: 0;
    width: 216px;
    height: 283px;
  }
  .stripes line {
    stroke: var(--gold);
    stroke-width: 4;
  }

  .slogan {
    position: absolute;
    transform: rotate(-22deg);
    transform-origin: 0 0;
    white-space: nowrap;
  }
  .band {
    display: table;
    background: var(--orange);
    color: var(--white);
    text-transform: uppercase;
    line-height: 1.08;
    padding: 1px 5px 0;
    margin-bottom: 4px;
    font-weight: 500;
    letter-spacing: 0;
  }
  .band strong { font-weight: 800; }
  .band--xl { font-size: 23px; font-weight: 700; }
  .band--lg { font-size: 18px; }
  .band--md { font-size: 15px; }
  .band--sm { font-size: 12px; }
  .band--xs { font-size: 8px; padding: 0 3px; }
  .band--bold { font-weight: 800; }

  .visual {
    position: absolute;
  }
  .visual--rock {
    left: 138px; top: 232px; width: 52px; height: 34px;
    background: linear-gradient(135deg, #d9dadf, var(--stone) 60%, #55575f);
    border-radius: 40% 50% 35% 45%;
  }
  .visual--team {
    left: 122px; top: 172px; width: 86px; height: 100px;
    background: linear-gradient(180deg, #141422, var(--ink));
    border-radius: 30px 30px 4px 4px;
  }
  .visual--thinker {
    left: 72px; top: 170px; width: 72px; height: 94px;
    background: var(--ink);
    border-radius: 40px 40px 8px 8px;
  }
  .visual--weary {
    left: 28px; top: 196px; width: 78px; height: 70px;
    background: linear-gradient(180deg, #5a3b28, var(--skin) 45%, #e9e3dc);
    border-radius: 40% 40% 10% 10%;
  }
  .visual--hourglass {
    left: 72px; top: 182px; width: 70px; height: 92px;
    background: linear-gradient(160deg, #e8c3a6, var(--skin) 50%, #8a5a32);
    border-radius: 30px 30px 14px 14px;
  }
</style>
</head>
<body>
<main class="sign-series">

  <section class="sign sign--rocks">
    <svg class="stripes" viewBox="0 0 216 283" aria-hidden="true">
      <line x1="-10" y1="140" x2="226" y2="45"/>
      <line x1="-10" y1="196" x2="226" y2="100"/>
      <line x1="-10" y1="232" x2="226" y2="137"/>
    </svg>
    <div class="slogan" style="left:8px; top:104px;">
      <span class="band band--xl">Are</span>
      <span class="band band--xl">You looking</span>
      <span class="band band--xl">Under</span>
      <span class="band band--xl" style="margin-left:58px;">Rocks?</span>
    </div>
    <div class="visual visual--rock" role="img" aria-label="Photo of a grey rock"></div>
  </section>

  <section class="sign sign--advocates">
    <svg class="stripes" viewBox="0 0 216 283" aria-hidden="true">
      <line x1="-10" y1="96" x2="226" y2="0"/>
      <line x1="-10" y1="150" x2="226" y2="55"/>
      <line x1="-10" y1="186" x2="226" y2="91"/>
    </svg>
    <div class="slogan" style="left:4px; top:80px;">
      <span class="band band--md">Are you</span>
      <span class="band band--lg band--bold">Creating</span>
      <span class="band band--md">Advocates</span>
    </div>
    <div class="slogan" style="left:112px; top:112px;">
      <span class="band band--md">Apathetics</span>
    </div>
    <div class="slogan" style="left:98px; top:140px;">
      <span class="band band--xs">or</span>
    </div>
    <div class="slogan" style="left:4px; top:186px;">
      <span class="band band--md">Apathetics</span>
    </div>
    <div class="visual visual--team" role="img" aria-label="Silhouettes of three businesspeople standing"></div>
  </section>

  <section class="sign sign--perception">
    <svg class="stripes" viewBox="0 0 216 283" aria-hidden="true">
      <line x1="-10" y1="84" x2="226" y2="-12"/>
      <line x1="-10" y1="132" x2="226" y2="37"/>
      <line x1="-10" y1="168" x2="226" y2="73"/>
    </svg>
    <div class="slogan" style="left:4px; top:98px;">
      <span class="band band--lg">A rep's perception</span>
      <span class="band band--sm" style="margin-left:30px;">Is <strong>your</strong></span>
      <span class="band band--xl" style="margin-left:36px;">Reality</span>
    </div>
    <div class="visual visual--thinker" role="img" aria-label="Silhouette of a head with a question mark"></div>
  </section>

  <section class="sign sign--mediocrity">
    <svg class="stripes" viewBox="0 0 216 283" aria-hidden="true">
      <line x1="-10" y1="92" x2="226" y2="-4"/>
      <line x1="-10" y1="146" x2="226" y2="51"/>
      <line x1="-10" y1="184" x2="226" y2="89"/>
    </svg>
    <div class="slogan" style="left:8px; top:104px;">
      <span class="band band--lg">Mediocrity</span>
      <span class="band band--sm" style="margin-left:24px;">Is</span>
      <span class="band band--xl" style="margin-left:14px; font-size:20px; font-weight:800;">Unacceptable</span>
    </div>
    <div class="visual visual--weary" role="img" aria-label="Photo of a tired man resting his head on his arms"></div>
  </section>

  <section class="sign sign--smart">
    <svg class="stripes" viewBox="0 0 216 283" aria-hidden="true">
      <line x1="-10" y1="70" x2="226" y2="-26"/>
      <line x1="-10" y1="122" x2="226" y2="27"/>
      <line x1="-10" y1="190" x2="226" y2="95"/>
    </svg>
    <div class="slogan" style="left:4px; top:86px;">
      <span class="band band--md">If you</span>
      <span class="band band--md">Don't stop to</span>
      <span class="band band--sm" style="font-size:11px;">Take the time to work <strong>smart</strong></span>
    </div>
    <div class="slogan" style="left:4px; top:178px;">
      <span class="band band--md" style="font-size:13px;">You'll never have enough</span>
      <span class="band band--md" style="font-size:13px;">Time to work <strong>hard</strong></span>
    </div>
    <div class="visual visual--hourglass" role="img" aria-label="Photo of a hand holding an hourglass"></div>
  </section>

</main>
</body>
</html>
```